Postcard Design - New Movers - Men only haircuts

Advertisement for "New Movers" into the local area. to try our hair curt facility. Our business is called Shearing Den; hair cuts for men and boys and can be found on FB using the words "Shearing Den, Pooler Georgia". Our décor is man cave.

```html
<!DOCTYPE html>
<html lang="en">
<head>
<meta charset="utf-8">
<title>Shearing Den – New Movers Postcard</title>
<link rel="stylesheet" href="https://fonts.googleapis.com/css2?family=Bebas+Neue&family=Fredoka:wght@400;500&family=Oswald:wght@400;500&display=swap">
<style>
  :root {
    --stage: #5a5a5a;
    --card-dark: #1c1c1c;
    --collage-a: #3a3a3a;
    --collage-b: #161616;
    --red: #e0222a;
    --white: #ffffff;
    --ink: #222222;
    --photo: #8a8a8a;
  }
  * { box-sizing: border-box; margin: 0; padding: 0; }
  html, body { width: 866px; height: 1200px; overflow: hidden; }
  body { background: var(--stage); position: relative; font-family: "Oswald", sans-serif; }

  .card { position: absolute; overflow: hidden; }
  .front { left: 68px; top: 6px; width: 732px; height: 582px; background: var(--card-dark); }
  .back { left: 68px; top: 606px; width: 732px; height: 560px; background: var(--white); }

  .collage { position: absolute; inset: 0; background: radial-gradient(ellipse at 50% 45%, var(--collage-a), var(--collage-b)); }
  .front-copy { position: absolute; inset: 0; color: var(--white); text-align: center; }

  .headline { font-family: "Bebas Neue", sans-serif; font-weight: 400; position: absolute; left: 0; right: 0; white-space: nowrap; }
  .headline-top { top: 54px; font-size: 86px; line-height: 76px; letter-spacing: 1px; }
  .headline-bottom { top: 142px; font-size: 68px; line-height: 58px; letter-spacing: 0.5px; }
  .headline-bottom .accent { color: var(--red); }
  .rule-white { position: absolute; left: 74px; right: 74px; height: 3px; background: var(--white); }
  .rule-one { top: 133px; }
  .rule-two { top: 202px; }

  .intro { position: absolute; left: 74px; right: 74px; top: 214px; font-family: "Bebas Neue", sans-serif; font-size: 16.5px; line-height: 19.5px; text-align: justify; text-align-last: left; letter-spacing: 0.2px; }

  .cta { position: absolute; left: 214px; top: 362px; width: 306px; height: 34px; background: var(--red); font-family: "Fredoka", sans-serif; font-size: 20px; line-height: 34px; }

  .brand-name { position: absolute; left: 0; right: 0; top: 410px; font-family: "Bebas Neue", sans-serif; font-size: 72px; line-height: 66px; letter-spacing: 9px; color: var(--white); white-space: nowrap; }
  .brand-tagline { position: absolute; left: 0; right: 0; top: 474px; font-family: "Oswald", sans-serif; font-weight: 500; font-size: 23px; line-height: 30px; letter-spacing: 2.5px; }

  .front-footer { position: absolute; left: 0; right: 0; top: 534px; height: 31px; background: var(--red); display: flex; align-items: center; justify-content: space-between; padding: 0 26px; font-family: "Bebas Neue", sans-serif; font-size: 18px; white-space: nowrap; }
  .front-footer .phone { display: flex; align-items: center; gap: 6px; font-size: 24px; }

  .back-panel { position: absolute; left: 0; top: 0; width: 352px; height: 560px; background: var(--card-dark); color: var(--white); }
  .back-panel .collage { background: linear-gradient(180deg, var(--collage-a), var(--collage-b)); }
  .back-brand { position: absolute; left: 0; right: 0; top: 18px; text-align: center; }
  .back-brand .brand-name-small { font-family: "Bebas Neue", sans-serif; font-size: 38px; line-height: 36px; letter-spacing: 5px; }
  .back-brand .brand-tagline-small { font-family: "Oswald", sans-serif; font-weight: 500; font-size: 12px; line-height: 16px; letter-spacing: 1px; }

  .services-bar { position: absolute; left: 0; top: 85px; width: 352px; height: 23px; background: var(--red); text-align: center; font-family: "Bebas Neue", sans-serif; font-size: 19px; line-height: 24px; }

  .service { position: absolute; left: 0; width: 352px; display: flex; }
  .service-photo { width: 72px; height: 88px; background: linear-gradient(160deg, var(--photo), #4a4a4a); flex: none; }
  .service-text { padding-left: 8px; }
  .service-title { font-family: "Fredoka", sans-serif; color: var(--red); font-size: 18px; line-height: 22px; }
  .service-body { font-family: "Bebas Neue", sans-serif; font-size: 15.5px; line-height: 21.5px; letter-spacing: 0.2px; }
  .service-cut { top: 120px; }
  .service-beard { top: 230px; }
  .service-kids { top: 348px; }
  .service-kids .service-photo { height: 84px; margin-top: 18px; }

  .rule-red { position: absolute; left: 8px; right: 8px; top: 474px; height: 2px; background: var(--red); }
  .back-contact { position: absolute; left: 10px; top: 486px; font-family: "Bebas Neue", sans-serif; font-size: 15.5px; line-height: 20px; }
  .back-contact .row { display: flex; gap: 6px; align-items: flex-start; }
  .back-contact .indent { padding-left: 16px; }

  .postage { position: absolute; left: 549px; top: 16px; width: 163px; height: 163px; border: 1px solid var(--ink); font-family: Arial, sans-serif; font-size: 15px; color: var(--ink); text-align: center; padding-top: 66px; line-height: 20px; }
  .address-line { position: absolute; left: 410px; width: 285px; height: 1px; background: var(--ink); }
  .address-line-1 { top: 266px; }
  .address-line-2 { top: 318px; }
  .address-line-3 { top: 372px; }
  .address-line-4 { top: 414px; }
</style>
</head>
<body>

<section class="card front">
  <div class="collage" role="img" aria-label="Grid of black and white portraits showing men's and boys' hairstyles"></div>
  <div class="front-copy">
    <h1 class="headline headline-top">Need a haircut?</h1>
    <div class="rule-white rule-one"></div>
    <h2 class="headline headline-bottom">A new salon for <span class="accent">mens only</span></h2>
    <div class="rule-white rule-two"></div>
    <p class="intro">We offers world-class haircuts for men and boys in the Harlan Ridge area. Our staff went through extensive training and has mastered virtually every style. Whether you want a vintage, classic, or modern look, we're the barber shop for you! We offer a "man cave" environment so you are able to come and relax in a place where we understand mens comfort and style.</p>
    <div class="cta">Make An Appoinment Now! At</div>
    <div class="brand-name">Shearing Den</div>
    <div class="brand-tagline">HAIRCUTS FOR MEN AND BOYS</div>
    <div class="front-footer">
      <span>218 W Elm St Unit 12 Harlan Ridge, GA 31399 (Between Maple Diner and Kenji's)</span>
      <span class="phone">
        <svg width="18" height="18" viewBox="0 0 24 24" aria-hidden="true"><path fill="#fff" d="M6.6 10.8a15.1 15.1 0 0 0 6.6 6.6l2.2-2.2a1 1 0 0 1 1-.25 11.4 11.4 0 0 0 3.6.57 1 1 0 0 1 1 1V20a1 1 0 0 1-1 1A17 17 0 0 1 3 4a1 1 0 0 1 1-1h3.5a1 1 0 0 1 1 1c0 1.25.2 2.45.57 3.57a1 1 0 0 1-.25 1z"/></svg>
        (912) 555-0147
      </span>
    </div>
  </div>
</section>

<section class="card back">
  <div class="back-panel">
    <div class="collage" role="img" aria-label="Faint grid of men's hairstyle portraits"></div>
    <div class="back-brand">
      <div class="brand-name-small">Shearing Den</div>
      <div class="brand-tagline-small">HAIRCUTS FOR MEN AND BOYS</div>
    </div>
    <div class="services-bar">Our Services</div>

    <div class="service service-cut">
      <div class="service-photo" role="img" aria-label="Photo of a man with a fresh styled haircut"></div>
      <div class="service-text">
        <div class="service-title">Haircut &amp; Style</div>
        <div class="service-body">Every haircut is executed with precision<br>and style. We promise you'll walk out of<br>here lookin' fresh.</div>
      </div>
    </div>

    <div class="service service-beard">
      <div class="service-photo" role="img" aria-label="Photo of a man with a groomed moustache"></div>
      <div class="service-text">
        <div class="service-title">Beard or Moustache Trim</div>
        <div class="service-body">Beards and moustaches are in. We will<br>make sure your burly friend is tamed and<br>styled to look better than ever.</div>
      </div>
    </div>

    <div class="service service-kids">
      <div class="service-photo" role="img" aria-label="Photo of a young boy getting a haircut"></div>
      <div class="service-text">
        <div class="service-title">Kids Cuts</div>
        <div class="service-body">We offer a fun experience for our cave<br>kids. We cut kids hair in a race car chair<br>that has lights, horn, and wheel that<br>turns. After the cut they will get to pick a<br>toy from our treasure chest.</div>
      </div>
    </div>

    <div class="rule-red"></div>
    <div class="back-contact">
      <div class="row">
        <svg width="10" height="16" viewBox="0 0 10 16" aria-hidden="true"><path fill="#e0222a" d="M5 0a5 5 0 0 0-5 5c0 4 5 11 5 11s5-7 5-11a5 5 0 0 0-5-5zm0 7a2 2 0 1 1 0-4 2 2 0 0 1 0 4z"/></svg>
        <span>218 W Elm St Unit 12 Harlan Ridge, GA 31399</span>
      </div>
      <div class="indent">(Between Maple Diner and Kenji's)</div>
      <div class="row">
        <svg width="12" height="14" viewBox="0 0 24 24" aria-hidden="true"><path fill="#e0222a" d="M6.6 10.8a15.1 15.1 0 0 0 6.6 6.6l2.2-2.2a1 1 0 0 1 1-.25 11.4 11.4 0 0 0 3.6.57 1 1 0 0 1 1 1V20a1 1 0 0 1-1 1A17 17 0 0 1 3 4a1 1 0 0 1 1-1h3.5a1 1 0 0 1 1 1c0 1.25.2 2.45.57 3.57a1 1 0 0 1-.25 1z"/></svg>
        <span>(912) 555-0147</span>
      </div>
    </div>
  </div>

  <div class="postage">Postage<br>Area</div>
  <div class="address-line address-line-1"></div>
  <div class="address-line address-line-2"></div>
  <div class="address-line address-line-3"></div>
  <div class="address-line address-line-4"></div>
</section>

</body>
</html>
```